Criação de Papelaria (6 itens) para Decoração & Arven Casa
A empresa queria:
" É um comércio de móveis planejados e móveis complementares, como sofás, cadeiras, banquetas e mesas. "

```html
<!DOCTYPE html>
<html lang="pt-BR">
<head>
<meta charset="utf-8">
<title>Arven Casa — Papelaria</title>
<link rel="stylesheet" href="https://fonts.googleapis.com/css2?family=Montserrat:wght@500&display=swap">
<style>
  :root {
    --backdrop: #e9e7e4;
    --paper: #f4f3f1;
    --ink-dark: #14161f;
    --ink-dark-soft: #1d2030;
    --wine: #6e2a30;
    --name-dark: #1b1b1f;
    --name-light: #ffffff;
    --contact: #d9dbe3;
  }
  * { box-sizing: border-box; margin: 0; padding: 0; }
  html, body {
    width: 1200px; height: 1200px; overflow: hidden;
    background: var(--backdrop);
    font-family: "Montserrat", sans-serif;
  }
  .stationery {
    width: 1200px; height: 1200px;
    display: flex; align-items: center; justify-content: center;
    gap: 80px;
  }
  .envelope, .card {
    position: relative;
    width: 440px; height: 620px;
    box-shadow: 0 18px 40px rgba(0,0,0,.18);
    overflow: hidden;
  }
  .envelope { background: var(--paper); }
  .envelope__flap {
    position: absolute; top: 0; left: 0; right: 0; height: 58px;
    background: var(--wine);
  }
  .card {
    background: radial-gradient(circle at 0% 50%, var(--ink-dark-soft) 0 300px, var(--ink-dark) 301px);
  }
  .company-name {
    position: absolute; left: 0; right: 0;
    text-align: center;
    font-weight: 500; font-size: 40px; letter-spacing: 6px;
    text-transform: uppercase;
    line-height: 1;
  }
  .envelope .company-name { color: var(--name-dark); top: 254px; }
  .card .company-name { color: var(--name-light); top: 228px; }
  .contact {
    position: absolute; left: 30px; right: 30px; bottom: 34px;
    display: grid; grid-template-columns: 1fr 1fr; gap: 9px 18px;
    color: var(--contact); font-size: 10.5px; font-weight: 500;
  }
  .contact__item { display: flex; align-items: center; gap: 6px; justify-content: flex-end; white-space: nowrap; }
  .contact__item--full { grid-column: 1 / -1; justify-content: center; }
  .contact svg { width: 11px; height: 11px; flex: none; fill: none; stroke: var(--contact); stroke-width: 2; }
</style>
</head>
<body>
<main class="stationery">
  <section class="envelope" aria-label="Envelope">
    <div class="envelope__flap"></div>
    <p class="company-name">Arven Casa</p>
  </section>

  <section class="card" aria-label="Cartão institucional">
    <p class="company-name">Arven Casa</p>
    <div class="contact">
      <div class="contact__item">+55 11 4000-1234
        <svg viewBox="0 0 24 24"><path d="M5 3h4l2 5-3 2a11 11 0 0 0 6 6l2-3 5 2v4a2 2 0 0 1-2 2A17 17 0 0 1 3 5a2 2 0 0 1 2-2z"/></svg>
      </div>
      <div class="contact__item">+55 11 9000-5678
        <svg viewBox="0 0 24 24"><rect x="7" y="2" width="10" height="20" rx="2"/><path d="M11 18h2"/></svg>
      </div>
      <div class="contact__item">contato@arvencasa.com.br
        <svg viewBox="0 0 24 24"><rect x="3" y="5" width="18" height="14" rx="1"/><path d="M3 6l9 7 9-7"/></svg>
      </div>
      <div class="contact__item">www.arvencasa.com.br
        <svg viewBox="0 0 24 24"><circle cx="12" cy="12" r="9"/><path d="M3 12h18M12 3c3 3 3 15 0 18M12 3c-3 3-3 15 0 18"/></svg>
      </div>
      <div class="contact__item contact__item--full">
        <svg viewBox="0 0 24 24"><path d="M12 22s7-7 7-12a7 7 0 0 0-14 0c0 5 7 12 7 12z"/><circle cx="12" cy="10" r="2.5"/></svg>
        R. das Acácias, 120
      </div>
    </div>
  </section>
</main>
</body>
</html>
```